依頼詳細
ECサイトのブランドコンセプトページ、商品ページ、プロモーションページのデザインをおねがいします。HTMLコーディングは含みません。

基本的な掲載コンテンツに変更はありません。添付のワイヤーを基に、フラワーショップのスイーツ店らしいシンプルで上品なデザインを希望します。作成頂いたコンセプトページをベースに他のページも制作したいと考えているため、その点も考慮して下さい。ロゴは添付ファイルのものを利用ください。

・デバイスフォントはWin "小塚ゴシック"、Mac "ヒラギノゴシック"、色がアースカラー。
・ターゲットは、30代~50代。スイーツ、花などの贈り物の購入者や、女子会、ホームパーティーでの購入者を想定。
・配色、クリエイティブは、参考サイトを参照。
[参考サイト]
http://www.mirelcafe.jp/
http://www.toviancosweets.co.jp/

サイトリリース時にデザインに手を加えることをご了承ください。

ご質問・ご確認事項ありましたら「この依頼に質問」からお願いします。
それではたくさんのご応募お待ちしております。
ページ数
3ページ
希望イメージ
シンプル 複雑
単色 カラフル
暗い 明るい
日常 高級
遊び心 厳粛
未来的 伝統的
女性的 男性的
希望する色
アースカラー、ピンク、ホワイト、
納品ファイル
• イラストレーター形式 (.ai)
• フォトショップ形式 (.psd)
補足説明
選定後納品ファイルですが、レイヤー情報を保持した.ai,.psdのいずれかを納品いただきます。当方、Win版CS5。
情報が少なかったので追記致します。

商品ページは全ての商品に共通したデザイン・キャッチコピーをおねがいします。
商品ページのイメージは下記サイトを参考にお願いします。

http://www.kumeyo8.com/menu/fruitcrumblepie/

プロモーションページは下記サイトのような特集を組んで商品ページに誘導するイメージです

http://www.velomiratte.com/new.php?twn=327
たくさんのご提案ありがとうございました。

選定にお時間をいただき申し訳ございません。
とても良い提案が多く、クライアントの方でも決めかねております。

現在、クライアントの方で当選候補者様を数名に絞っていただいてるのですが、クライアントから候補者様のデザインされたプロモーションページが見たいという要望がございまして、ご応募いただいたランサー様に大至急、プロモーションページのデザインをお願い致します。当選候補者様には個別で修正依頼として、お願いを致します。修正依頼のないランサー様には申し訳ございませんが、ご了承ください。

プロモーションページをご提案いただけた方の中から必ず当選者を選ばせて頂くことを確約致します。
ご対応いただいている皆様
要件急変、大変申し訳ございません。

クライアントの方でこんなイメージも見たい、あんなイメージも見たいと意見が二転三転しておりまして、あれもこれもと対応していただくわけにはいかないので、ナビの画像など無しで小さめのおしゃれなフォントにしていただくだけで構いません。
プロモーションのページについては下記参考サイトのような白背景にフォントと余白で魅せるデザインでお願いできないでしょうか?

レイアウトはワイヤーの通りで構いません。

参考:http://nuwabe-online.com/

お手数おかけして申し訳ございませんが、何卒よろしくお願い致します。

急な変更にご対応いただいているランサー様。
ありがとうございます。

ご提案いただいた案は全て、クライアントに提示致します。
ご提案いただいた案の中から必ず当選者を確定することを約束致します。

当選者のランサー様には当選したデザイン案でのブランドコンセプトページ、
商品ページの修正をお願い致します。お手数ではございますが、何卒ご了承くださいますようよろしくお願い申し上げます。
急な変更にも関わらず、ご対応いただきましたランサーの皆様、ありがとうございます。

現在、ご提案いただいたプロモーションページのデザインをクライアントに提出し選定中でございます。

提出致しましたデザインの中から当選者様を選ばせて頂きます。

当選者様には、お手数ではございますが、当選デザインでの商品ページ、コンセプトページの修正をお願い致しますこと、ご了承くださいますようお願い申し上げます。
当選者様は決定しているのですが、まだ修整をお願いすることがございまして、当選の確定を控えさせていただいております。

ご提案を頂いたランサーの皆様がたには、当選の確定をお待たせしてしまっていることお詫び申し上げます。
■ 選んだ理由

シンプルな中にも品があり、クライアント様の受けもよく、度重なる修正のお願いにもご対応いただき、クライアント様のイメージに近づけることができました。ありがとうございます。

■ 提案者全員のお礼・コメント

急な要件変更にも関わらず、ご対応いただきましたランサーの皆様、ありがとうございました。

```html
<!DOCTYPE html>
<html lang="ja">
<head>
<meta charset="utf-8">
<title>コンセプト | Bloom Patisserie</title>
<link href="https://fonts.googleapis.com/css2?family=Noto+Sans+JP:wght@400;500;700&family=Noto+Serif+JP:wght@500;700&family=Parisienne&display=swap" rel="stylesheet">
<style>
:root{
  --pink:#e6929d;
  --pink-deep:#d86f80;
  --pink-pale:#fbecee;
  --pink-soft:#f6d7db;
  --brown:#6a3b2c;
  --brown-soft:#8a6a5c;
  --text:#5a4a44;
  --line:#e9c9cd;
  --white:#ffffff;
}
*{margin:0;padding:0;box-sizing:border-box}
html,body{width:706px;height:1200px;overflow:hidden}
body{position:relative;background:var(--white);font-family:"Noto Sans JP",sans-serif;color:var(--text);font-size:9px;line-height:1.7}
.topbar{position:absolute;left:0;top:0;width:706px;height:20px;background:var(--pink-pale);display:flex;justify-content:space-between;align-items:center;padding:0 16px;font-size:8px;color:var(--brown-soft)}
.topbar ul{display:flex;gap:14px;list-style:none}
.topbar li::before{content:"";display:inline-block;width:6px;height:6px;background:var(--pink);border-radius:50%;margin-right:4px;vertical-align:middle}
.header{position:absolute;left:0;top:20px;width:706px;height:92px;background:var(--white)}
.logo{position:absolute;left:20px;top:34px;display:flex;align-items:center;gap:6px;font-family:"Noto Serif JP",serif;font-weight:700;font-size:15px;color:var(--brown);white-space:nowrap}
.logo .mark{width:9px;height:9px;border-radius:50%;background:var(--pink)}
.gnav{position:absolute;left:182px;top:0;display:flex;list-style:none}
.gnav li{width:84px;height:92px;display:flex;flex-direction:column;align-items:center;justify-content:center;border-left:1px dotted var(--line);font-size:10px;color:var(--brown);font-weight:500;white-space:nowrap}
.gnav li:last-child{border-right:1px dotted var(--line)}
.gnav li span{font-family:"Parisienne",cursive;font-size:11px;color:var(--pink);font-weight:400}
.gnav li.is-current{background:var(--pink-pale)}
.band{position:absolute;left:0;top:112px;width:706px;height:26px;background:linear-gradient(var(--pink-soft),var(--pink-pale))}
.crumb{position:absolute;left:176px;top:150px;font-size:9px;color:var(--brown-soft)}
.crumb a{color:var(--pink-deep)}
.side{position:absolute;left:18px;top:146px;width:142px}
.product-box{border:3px double var(--pink);border-radius:8px;padding:10px 10px 12px;background:var(--white)}
.product-box h2{text-align:center;font-family:"Parisienne",cursive;font-size:20px;color:var(--pink-deep);font-weight:400;line-height:1.1}
.product-box h2 small{display:block;font-family:"Noto Sans JP",sans-serif;font-size:8px;color:var(--brown-soft)}
.product-box ul{list-style:none;margin-top:10px}
.product-box li{display:flex;gap:7px;align-items:center;padding:6px 0;border-bottom:1px dotted var(--line);font-size:9px;color:var(--brown);line-height:1.2}
.product-box li i{width:18px;height:18px;border-radius:3px;background:var(--pink-soft);flex:none}
.product-box li em{display:block;font-style:normal;font-family:"Parisienne",cursive;color:var(--pink);font-size:10px}
.promo{height:112px;margin-top:10px;background:linear-gradient(135deg,#f7dde0,#fdf4f3 60%,#efc9cd);position:relative}
.promo span{position:absolute;left:10px;top:12px;font-family:"Parisienne",cursive;font-size:20px;color:var(--white)}
.calendar{margin-top:16px;border:1px solid var(--brown);font-size:8px}
.calendar header{background:var(--brown);color:var(--white);text-align:center;padding:4px 0;line-height:1.1}
.calendar header b{display:block;font-size:24px;font-family:"Noto Serif JP",serif}
.calendar table{width:100%;border-collapse:collapse;text-align:center;color:var(--brown)}
.calendar td{padding:1px 0}
.calendar .off{color:var(--pink-deep)}
.cal-note{font-size:7px;color:var(--pink-deep);margin-top:3px}
.main{position:absolute;left:176px;top:170px;width:510px}
.title-box{height:58px;border:1px solid var(--line);border-radius:4px;text-align:center;padding-top:10px;font-family:"Noto Serif JP",serif;font-size:20px;color:var(--brown);background:linear-gradient(var(--white),var(--pink-pale))}
.lead{margin-top:14px;padding:0 8px;font-size:9px;line-height:17px;background-image:repeating-linear-gradient(transparent 0 16px,var(--line) 16px 17px)}
.feature{position:absolute;left:0;top:345px;width:510px;height:170px;background:linear-gradient(90deg,#d9707f,#ea9ca5 60%,#f3c4c8);color:var(--white)}
.feature h2{position:absolute;left:14px;top:24px;font-family:"Noto Serif JP",serif;font-size:24px;font-weight:500;line-height:1.1}
.feature h2 span{display:block;font-family:"Parisienne",cursive;font-size:16px;font-weight:400;margin-top:4px}
.feature p{position:absolute;left:14px;top:98px;width:480px;font-size:9px;line-height:1.8}
.feature .visual{position:absolute;right:0;top:0;width:200px;height:86px;background:linear-gradient(135deg,#f4c4c9,#fbe7e8);opacity:.85}
.article{position:absolute;left:0;top:515px;width:510px;height:380px;font-size:9px;line-height:1.9}
.article .photo{position:absolute;border:3px solid var(--white);box-shadow:0 0 0 1px var(--line)}
.photo.field{left:330px;top:35px;width:130px;height:118px;background:linear-gradient(#7d8f5a,#a34b4f 55%,#5e6b3c)}
.photo.rose{left:12px;top:190px;width:165px;height:130px;background:radial-gradient(circle at 45% 50%,#c4253a,#8e1826 45%,#4f6b33 75%)}
.t1{position:absolute;left:12px;top:40px;width:300px}
.t2{position:absolute;left:196px;top:196px;width:300px}
.t3{position:absolute;left:12px;top:345px;width:490px}
.pagetop{position:absolute;left:610px;top:1092px;font-family:"Parisienne",cursive;color:var(--pink-deep);font-size:12px}
.footer{position:absolute;left:0;top:1160px;width:706px;height:40px;background:var(--pink-soft);text-align:center;line-height:40px;font-size:8px;color:var(--brown)}
</style>
</head>
<body>
<div class="topbar">
  <span>Bloom Patisserieのオンラインショップ</span>
  <ul><li>新規会員登録</li><li>ログイン</li><li>マイページ</li><li>カートを見る</li></ul>
</div>
<header class="header">
  <div class="logo"><span class="mark"></span>Bloom Patisserie</div>
  <ul class="gnav">
    <li class="is-current">ホーム<span>Home</span></li>
    <li>コンセプト<span>Concept</span></li>
    <li>プロダクト<span>Products</span></li>
    <li>ギフト<span>Gift</span></li>
    <li>ご利用ガイド<span>Guide</span></li>
    <li>お問い合わせ<span>Contact</span></li>
  </ul>
</header>
<div class="band"></div>
<p class="crumb"><a>Home</a> ＞ コンセプト</p>

<aside class="side">
  <section class="product-box">
    <h2>Product<small>商品から選ぶ</small></h2>
    <ul>
      <li><i></i><div>チーズケーキ<em>Cheese cake</em></div></li>
      <li><i></i><div>ロールケーキ<em>Roll cake</em></div></li>
      <li><i></i><div>フルーツタルト<em>Fruit tart</em></div></li>
      <li><i></i><div>焼き菓子<em>Baked sweets</em></div></li>
      <li><i></i><div>プレートケーキ<em>Plate cake</em></div></li>
      <li><i></i><div>ブレンド<em>Blend tea</em></div></li>
    </ul>
  </section>
  <div class="promo" role="img" aria-label="パステルカラーのマカロン写真"><span>Macarons</span></div>
  <div class="promo" role="img" aria-label="マカロンの詰め合わせ写真"><span>Macarons</span></div>
  <section class="calendar">
    <header><b>11</b>November</header>
    <table>
      <tr><td class="off">日</td><td>月</td><td>火</td><td>水</td><td>木</td><td>金</td><td>土</td></tr>
      <tr><td></td><td></td><td></td><td>1</td><td>2</td><td>3</td><td>4</td></tr>
      <tr><td class="off">5</td><td>6</td><td>7</td><td>8</td><td>9</td><td>10</td><td>11</td></tr>
      <tr><td class="off">12</td><td>13</td><td>14</td><td>15</td><td>16</td><td>17</td><td>18</td></tr>
      <tr><td class="off">19</td><td>20</td><td>21</td><td>22</td><td>23</td><td>24</td><td>25</td></tr>
      <tr><td class="off">26</td><td>27</td><td>28</td><td>29</td><td>30</td><td></td><td></td></tr>
    </table>
  </section>
  <p class="cal-note">赤字は店休日のため発送をお休みします</p>
</aside>

<main class="main">
  <h1 class="title-box">お客さまへ</h1>
  <div class="lead">
    <p>私たちはお花とお菓子で、ギフトのひとときをより華やかに彩りたいと考えています。</p>
    <p>季節のお花を感じる素材を選び、ひとつひとつ丁寧に仕上げています。</p>
    <p>「笑顔を届けるスイーツ」をテーマに、贈る方にも受け取る方にも喜んでいただける</p>
    <p>ケーキや焼き菓子をご用意しました。</p>
    <p>BLOOM PATISSERIEのお菓子が、大切な方との特別な時間を彩るお手伝いになれば幸いです。</p>
    <p>お祝いの席や女子会、ホームパーティーにもぜひご利用ください。</p>
    <p>一つひとつのお菓子に、花のようなやさしさを込めてお届けいたします。</p>
    <p>今後とも変わらぬご愛顧を賜りますよう、よろしくお願い申し上げます。</p>
  </div>

  <section class="feature">
    <div class="visual" role="img" aria-label="淡いピンクの花びらの写真"></div>
    <h2>素材へのこだわり<span>Attention to material</span></h2>
    <p>BLOOM PATISSERIEは素材の一つひとつにこだわり、花の香りを生かしたお菓子づくりを続けています。<br>季節の恵みを大切に、心を込めてお届けします。</p>
  </section>

  <section class="article">
    <p class="t1">自社農園で育てた「香りのバラ」を使用しています。<br>農薬を控え、手作業で丁寧に育てた花びらだけを<br>BLOOM PATISSERIEのお菓子に贅沢に使っています。</p>
    <div class="photo field" role="img" aria-label="バラ畑の通路の写真"></div>
    <div class="photo rose" role="img" aria-label="赤いバラの花の写真"></div>
    <p class="t2">香りのバラ「ルミエ」は、ほのかな甘さと華やかな<br>香りが特徴です。開花の一番よい時期に摘み取り、<br>自然な色と香りをそのままお菓子に閉じ込めました。</p>
    <p class="t3">また、日本でも数少ない食用バラ農園と契約し、<br>安心してお召し上がりいただける素材だけを厳選しています。</p>
  </section>
</main>
<p class="pagetop">▲ Page Top</p>
<footer class="footer">Copyright © Bloom Patisserie all right reserved.</footer>
</body>
</html>
```